Veterinary Power Point Template/Master

Dear Creatives,
we would need a Power Point Template that can be used for internal and external presentations. It'll mostly be needed to create B2B presentations at congresses or seminars, at which our vets attend as podium guests and lecturers.

What is important?
We see ourselves as highly professional, clean and innovative. One of our greatest mission is to build our work on latest medical research and the latest technology within veterinary medicine.
Therefore, our design should represent exactly this and look modern, professional and clinical.

Which slides do we need? What should they include?
- title
- section slides
- agenda
- Team slides to introduce our personell
- classic title & content
- slides to include different media and text options
- page numbers
- date
- our logo
- icons (if possible)

Unfortunately, we do not have an english version of our website yet, but feel free to browse through it to get a feeling for our appearance and values: https://www.tierpraxolan.at

We will also attach our little brand booklet as a guidance for you. BUT feel free to think out of the box and create a beautiful PPT design which is fun to watch.

Thrilled to see your great work already!

Target Market(s)

Austria

Industry/Entity Type

veterinary medicine

Font styles to use
Sans Serif
Other font styles liked:
• please only use Roboto font

Requirements
Must have
• items described in the creative brief
Nice to have
• animations and fancy transitions
Should not have
• Comic Sans or classic PPT Preset Designs

```html
<!DOCTYPE html>
<html lang="en">
<head>
<meta charset="utf-8">
<title>Tierpraxolan Pitch Deck Template</title>
<link href="https://fonts.googleapis.com/css2?family=Baloo+2:wght@500;700;800&family=Hind:wght@400;500;600&display=swap" rel="stylesheet">
<style>
:root{
  --stage:#8596a8;
  --navy:#243447;
  --gold:#c99a00;
  --rust:#b5471a;
  --green:#0a9e73;
  --brown:#3d1e0e;
  --white:#ffffff;
  --text:#5b6573;
  --line:#e6e9ee;
}
*{margin:0;padding:0;box-sizing:border-box}
html,body{width:1200px;height:4296px;overflow:hidden}
body{background:var(--stage);position:relative;font-family:"Hind",sans-serif;color:var(--navy)}
.slide{position:absolute;left:108px;width:983px;height:538px;background:var(--white);overflow:hidden;box-shadow:0 8px 24px rgba(20,30,45,.18)}
.slide--dark{background:var(--navy);color:var(--white)}
.abs{position:absolute}
.sidebar{position:absolute;left:0;top:0;width:63px;height:100%;background:var(--navy)}
.sidebar .mark{position:absolute;left:16px;top:16px;width:31px;height:31px;border-radius:50%;background:var(--white)}
.sidebar .url{position:absolute;left:32px;bottom:20px;transform-origin:0 0;transform:rotate(-90deg) translateY(-50%);font-size:12px;color:#c9d1db;white-space:nowrap}
.sidebar .num{position:absolute;left:17px;bottom:14px;width:29px;height:29px;border-radius:50%;background:var(--white);color:var(--navy);font-size:12px;display:flex;align-items:center;justify-content:center}
.corner-mark{position:absolute;right:18px;top:18px;width:30px;height:30px;border-radius:50%;border:2px solid var(--navy);background:var(--white)}
.page-num{position:absolute;right:24px;bottom:16px;width:32px;height:32px;border-radius:50%;background:var(--navy);color:var(--white);font-size:12px;display:flex;align-items:center;justify-content:center}
.foot-url{position:absolute;left:32px;bottom:30px;font-size:11px;color:var(--navy)}
.brand{position:absolute;display:flex;align-items:center;gap:12px}
.brand .dot{width:46px;height:46px;border-radius:50%;border:3px solid var(--gold);background:var(--white)}
.brand .name{font-family:"Baloo 2",sans-serif;font-weight:700;font-size:26px;letter-spacing:-.5px}
.title{font-family:"Baloo 2",sans-serif;font-weight:700;font-size:34px;line-height:50px}
.sub{font-size:14px;line-height:28px}
.ring{position:absolute;border-radius:50%;border:8px solid var(--gold)}
.dots{position:absolute;display:flex;gap:11px}
.dots i{width:13px;height:13px;border-radius:50%;display:block}
.dots i:nth-child(1){background:var(--rust)}
.dots i:nth-child(2){background:var(--green)}
.dots i:nth-child(3){background:var(--brown)}
.heading{position:absolute;font-family:"Baloo 2",sans-serif;font-weight:800;font-size:44px;line-height:57px;color:var(--navy)}
.para{position:absolute;font-size:16px;line-height:28px;color:var(--text)}
.small{font-size:11px;line-height:18px;color:var(--text)}
.badge{position:absolute;width:84px;height:84px;border-radius:50%;background:var(--white);box-shadow:0 4px 14px rgba(0,0,0,.15);display:flex;flex-direction:column;align-items:center;justify-content:center}
.badge b{font-family:"Baloo 2",sans-serif;font-size:19px;line-height:20px}
.badge span{font-size:8px;color:var(--text)}
.stats{position:absolute;left:467px;top:217px;width:470px;height:126px;background:var(--white);box-shadow:0 6px 20px rgba(0,0,0,.08);display:flex;align-items:center}
.stat{flex:1;height:100%;display:flex;flex-direction:column;align-items:center;justify-content:center;font-family:"Baloo 2",sans-serif}
.stat b{font-size:21px;line-height:26px}
.stat span{font-size:12px;font-weight:700}
.stat--hi{background:var(--gold);color:var(--white);flex:0 0 130px}
.sec-label{position:absolute;font-family:"Baloo 2",sans-serif;font-weight:700;font-size:22px}
.mission-item{position:absolute;left:470px;display:flex;align-items:center;gap:18px}
.mission-item .ic{width:36px;height:36px;border-radius:50%;border:1px solid #cfd5dc;display:flex;align-items:center;justify-content:center}
.kpi{position:absolute;padding-left:20px;border-left:2px solid var(--gold)}
.kpi b{display:block;font-family:"Baloo 2",sans-serif;font-weight:700;font-size:26px;line-height:30px}
.kpi p{margin-top:8px;width:160px}
.drop{position:absolute;top:207px;width:253px;height:240px}
.drop .val{position:absolute;left:40px;top:26px;font-family:"Baloo 2",sans-serif;font-weight:500;font-size:28px;color:var(--white)}
.drop .txt{position:absolute;left:40px;top:70px;width:185px;font-size:12px;line-height:18px;color:var(--white)}
.drop .icon{position:absolute;left:126px;top:156px;width:74px;height:74px;border-radius:50%;background:var(--white);box-shadow:0 6px 16px rgba(0,0,0,.18);display:flex;align-items:center;justify-content:center}
</style>
</head>
<body>

<!-- Title, dark -->
<section class="slide slide--dark" style="top:107px">
  <div class="brand" style="left:83px;top:103px"><span class="dot"></span><span class="name">Tierpraxolan</span></div>
  <h1 class="title abs" style="left:83px;top:205px">Pitch Deck<br>PowerPoint Template</h1>
  <p class="sub abs" style="left:83px;top:330px">Presentation Subtitle Goes Here<br>September 2023</p>
  <p class="abs" style="left:83px;top:470px;font-size:13px">www.tierpraxolan.at</p>
  <div class="ring" style="left:575px;top:43px;width:434px;height:434px;background:var(--white)"></div>
</section>

<!-- Title, light -->
<section class="slide" style="top:697px">
  <div class="sidebar"><span class="mark"></span><span class="url">www.tierpraxolan.at</span></div>
  <div class="brand" style="left:108px;top:100px"><span class="dot"></span><span class="name">Tierpraxolan</span></div>
  <h1 class="title abs" style="left:108px;top:202px">Pitch Deck<br>PowerPoint Template</h1>
  <p class="sub abs" style="left:108px;top:330px;color:var(--text)">Presentation Subtitle Goes Here<br>September 2023</p>
  <div class="ring" style="left:592px;top:43px;width:434px;height:434px;background:var(--navy)"></div>
</section>

<!-- Welcome with photo -->
<section class="slide" style="top:1287px">
  <div class="sidebar"><span class="mark"></span><span class="url">tierpraxolan.at</span><span class="num">3</span></div>
  <div class="abs" role="img" aria-label="Portrait of a brown dog against a golden arch" style="left:167px;top:130px;width:275px;height:325px;border-radius:140px 140px 150px 150px;background:linear-gradient(160deg,#d6a30f,#c99a00 55%,#a55f2c);box-shadow:0 14px 30px rgba(0,0,0,.15)"></div>
  <div class="badge" style="left:123px;top:280px;border:1px solid var(--green)"><b>976+</b><span>Active Client</span></div>
  <div class="badge" style="left:356px;top:360px;border:1px solid var(--rust)"><b style="color:var(--rust)">39+</b><span>Project Done</span></div>
  <div class="dots" style="left:542px;top:189px"><i></i><i></i><i></i></div>
  <h2 class="heading" style="left:540px;top:205px">Welcome To<br>Tierpraxolan</h2>
  <p class="para" style="left:542px;top:332px;width:340px">Lorem ipsum dolor sit amet, consectetuer adipiscing elit. Maecenas porttitor.</p>
</section>

<!-- Welcome with stats -->
<section class="slide" style="top:1877px">
  <div class="sidebar"><span class="mark"></span><span class="url">tierpraxolan.at</span><span class="num">4</span></div>
  <div class="dots" style="left:122px;top:176px"><i></i><i></i><i></i></div>
  <h2 class="heading" style="left:120px;top:193px">Welcome To<br>Tierpraxolan</h2>
  <p class="para" style="left:122px;top:318px;width:340px">Lorem ipsum dolor sit amet, consectetuer adipiscing elit. Maecenas porttitor.</p>
  <div class="stats">
    <div class="stat"><b>4</b><span>Brach Clinic</span></div>
    <div class="stat stat--hi"><b>70K+</b><span>Hours</span></div>
    <div class="stat"><b>12</b><span>Doctors</span></div>
    <div class="stat"><b>1200+</b><span>Vaccine Done</span></div>
  </div>
</section>

<!-- About us -->
<section class="slide" style="top:2467px">
  <div class="abs" role="img" aria-label="Portrait of a veterinarian in a white coat with a stethoscope" style="left:53px;top:47px;width:369px;height:428px;border-radius:16px;background:linear-gradient(180deg,#d3d8dd,#b8c2cc 60%,#c9d6e6)"></div>
  <span class="corner-mark"></span>
  <div class="dots" style="left:470px;top:53px"><i></i><i></i><i></i></div>
  <h2 class="heading" style="left:468px;top:72px;font-size:40px">About Us</h2>
  <p class="small abs" style="left:470px;top:127px;width:440px">Lorem ipsum dolor sit amet, consectetuer adipiscing elit. Maecenas porttitor congue massa. Fusce posuere, magna sed pulvinar ultricies, purus.</p>
  <h3 class="sec-label" style="left:468px;top:180px">Vision</h3>
  <p class="small abs" style="left:470px;top:222px;width:440px">Lorem ipsum dolor sit amet, consectetuer adipiscing elit. Maecenas porttitor congue massa. Fusce posuere, magna sed pulvinar ultricies, purus lectus.</p>
  <h3 class="sec-label" style="left:468px;top:276px">Mission</h3>
  <div class="mission-item" style="top:318px"><span class="ic"><svg width="18" height="18" viewBox="0 0 18 18" fill="none" stroke="#243447" stroke-width="1.4"><path d="M9 2v14M2 9h14"/></svg></span><p class="small">Lorem ipsum dolor sit amet, consectetuer adipiscing elit.<br>Maecenas porttitor congue massa.</p></div>
  <div class="mission-item" style="top:372px"><span class="ic"><svg width="18" height="18" viewBox="0 0 18 18" fill="none" stroke="#243447" stroke-width="1.4"><rect x="3" y="5" width="12" height="10"/><path d="M6 5V3h6v2M9 8v4M7 10h4"/></svg></span><p class="small">Lorem ipsum dolor sit amet, consectetuer adipiscing elit.<br>Maecenas porttitor congue massa.</p></div>
  <div class="mission-item" style="top:426px"><span class="ic"><svg width="18" height="18" viewBox="0 0 18 18" fill="none" stroke="#243447" stroke-width="1.4"><path d="M9 15s-6-3.6-6-8a3 3 0 0 1 6-1 3 3 0 0 1 6 1c0 4.4-6 8-6 8z"/></svg></span><p class="small">Lorem ipsum dolor sit amet, consectetuer adipiscing elit.<br>Maecenas porttitor congue massa.</p></div>
  <span class="foot-url">tierpraxolan.at</span>
  <span class="page-num">5</span>
</section>

<!-- Performances -->
<section class="slide" style="top:3057px">
  <span class="corner-mark"></span>
  <div class="dots" style="left:65px;top:41px"><i></i><i></i><i></i></div>
  <h2 class="heading" style="left:63px;top:60px;font-size:40px;line-height:53px">Tierpraxolan<br>Peformances</h2>
  <p class="small abs" style="left:478px;top:88px;width:420px;font-size:12px;line-height:25px">Lorem ipsum dolor sit amet, consectetuer adipiscing elit. Maecenas porttitor congue massa. Fusce posuere, magna sed pulvinar ultricies, purus lectus malesuada.</p>
  <svg class="abs" style="left:0;top:185px" width="345" height="353" viewBox="0 0 345 353">
    <path d="M0 40 Q60 0 150 15 Q215 30 200 110 L0 353 Z" fill="#c99a00"/>
    <path d="M345 110 Q345 40 290 60 Q230 90 200 353 L262 353 Q345 230 345 110 Z" fill="#243447"/>
  </svg>
  <div class="abs" role="img" aria-label="Photo of a husky dog sitting" style="left:60px;top:185px;width:230px;height:353px;border-radius:90px 90px 0 0;background:linear-gradient(180deg,#6b6660,#9c958c 50%,#d9d3c9)"></div>
  <div class="kpi" style="left:492px;top:228px"><b>400+</b><p class="small">Lorem ipsum dolor sit amet, consectetuer adipi elit.</p></div>
  <div class="kpi" style="left:700px;top:228px"><b>400+</b><p class="small">Lorem ipsum dolor sit amet, consectetuer adipi elit.</p></div>
  <div class="kpi" style="left:492px;top:348px"><b>400+</b><p class="small">Lorem ipsum dolor sit amet, consectetuer adipi elit.</p></div>
  <div class="kpi" style="left:700px;top:348px"><b>400+</b><p class="small">Lorem ipsum dolor sit amet, consectetuer adipi elit.</p></div>
  <span class="page-num">6</span>
</section>

<!-- Statistics -->
<section class="slide" style="top:3647px">
  <span class="corner-mark"></span>
  <div class="dots" style="left:65px;top:41px"><i></i><i></i><i></i></div>
  <h2 class="heading" style="left:63px;top:60px;font-size:40px;line-height:53px">Tierpraxolan<br>Statistics</h2>
  <p class="small abs" style="left:478px;top:88px;width:420px;font-size:12px;line-height:25px">Lorem ipsum dolor sit amet, consectetuer adipiscing elit. Maecenas porttitor congue massa. Fusce posuere, magna sed pulvinar ultricies, purus lectus malesuada.</p>

  <div class="drop" style="left:72px">
    <svg width="253" height="215" viewBox="0 0 253 215"><path d="M22 0H231Q253 0 250 25Q240 110 175 185Q160 200 140 200H110Q20 120 3 30Q0 0 22 0Z" fill="#b5471a"/></svg>
    <span class="val">400+</span>
    <p class="txt">Lorem ipsum dolor sit amet, consectetuer adipiscing elit. Maecenas porttitor cong.</p>
    <span class="icon"><svg width="30" height="30" viewBox="0 0 30 30" fill="none" stroke="#243447" stroke-width="1.5"><rect x="5" y="10" width="20" height="14" rx="2"/><path d="M15 13v8M11 17h8M11 10V7h8v3"/></svg></span>
  </div>
  <div class="drop" style="left:365px">
    <svg width="253" height="215" viewBox="0 0 253 215"><path d="M22 0H231Q253 0 250 25Q240 110 175 185Q160 200 140 200H110Q20 120 3 30Q0 0 22 0Z" fill="#0a9e73"/></svg>
    <span class="val">400+</span>
    <p class="txt">Lorem ipsum dolor sit amet, consectetuer adipiscing elit. Maecenas porttitor cong.</p>
    <span class="icon"><svg width="30" height="30" viewBox="0 0 30 30" fill="none" stroke="#243447" stroke-width="1.5"><path d="M4 12h22M6 12v13h18V12M5 12l3-6h14l3 6M12 25v-7h6v7"/></svg></span>
  </div>
  <div class="drop" style="left:659px">
    <svg width="253" height="215" viewBox="0 0 253 215"><path d="M22 0H231Q253 0 250 25Q240 110 175 185Q160 200 140 200H110Q20 120 3 30Q0 0 22 0Z" fill="#3d1e0e"/></svg>
    <span class="val">400+</span>
    <p class="txt">Lorem ipsum dolor sit amet, consectetuer adipiscing elit. Maecenas porttitor cong.</p>
    <span class="icon"><svg width="30" height="30" viewBox="0 0 30 30" fill="none" stroke="#243447" stroke-width="1.5"><path d="M15 25s-9-5.4-9-12a4.5 4.5 0 0 1 9-1.5A4.5 4.5 0 0 1 24 13c0 6.6-9 12-9 12z"/></svg></span>
  </div>

  <span class="foot-url">tierpraxolan.at</span>
  <span class="page-num">7</span>
</section>

</body>
</html>
```